A Quiet Harvest Book Cover Design

I require a book cover design to be completed for my book "A Quiet Harvest" How to build a highly profitable sports store!

This is my third attempt at engaging a graphic designer for this project. My last attempt was a terrible experience and ended up costing me more than double my original budget.

The successful designer will be engaged for more monthly jobs as they come to hand which would be brochure designs, web graphics etc.

I'm initially looking for this cover to drive online engagement, and sell this manuscript on Lumora with the vision to later roll out a hard copy in 6-12 months time.

My business is called The Fennick Crew - I'm a retail expert consultant who specialises in advanced shop floor retail solutions. I've worked with some of Australia's largest sporting goods retailers and have trained over 5000 employees. My goal is to inspire retail standards to greater levels, and continue helping to this industry employ millions of people around the world. I'm known for inspiring my clients to pivot their retail approach to more sustainable and long term strategies.

Please find attached a design brief.

Any questions, please ask upfront.

*important* all designers read the design brief thoroughly.

```html
<!DOCTYPE html>
<html lang="en">
<head>
<meta charset="utf-8">
<title>A Quiet Harvest – Book Cover</title>
<link rel="stylesheet" href="https://fonts.googleapis.com/css2?family=Anton&family=Oswald:wght@500;700&family=Arimo:ital,wght@0,400;0,700;1,700&display=swap">
<style>
  :root {
    --sky-deep: #0b1f6e;
    --sky-mid: #1f4fb8;
    --sky-bright: #4f8fe6;
    --sky-haze: #9cc3f0;
    --street-dark: #0a0f2a;
    --street-violet: #3b3f8f;
    --facade-glow: #8c90dc;
    --title-fill: #aab9dc;
    --title-edge: #1d2a5a;
    --spine-fill: #c7d2ea;
    --text-white: #ffffff;
    --rule: #c9d3ea;
    --portrait: #8a7f78;
  }
  * { margin: 0; padding: 0; box-sizing: border-box; }
  html, body { width: 1200px; height: 873px; overflow: hidden; background: #000; }
  .cover {
    position: relative; width: 1200px; height: 873px; overflow: hidden;
    font-family: "Arimo", Arial, sans-serif; color: var(--text-white);
  }
  .sky {
    position: absolute; inset: 0;
    background:
      radial-gradient(ellipse 420px 260px at 930px 330px, var(--sky-haze) 0%, rgba(156,195,240,0) 70%),
      radial-gradient(ellipse 500px 200px at 300px 520px, rgba(120,170,230,.55) 0%, rgba(120,170,230,0) 70%),
      linear-gradient(100deg, var(--sky-deep) 0%, var(--sky-mid) 45%, var(--sky-bright) 75%, var(--sky-mid) 100%);
  }
  .ground {
    position: absolute; left: 0; right: 0; bottom: 0; height: 60px;
    background: linear-gradient(180deg, rgba(10,30,20,0) 0%, #0c1a12 100%);
  }
  .street-scene {
    position: absolute; left: 600px; top: 380px; width: 600px; height: 493px;
    background:
      radial-gradient(ellipse 190px 230px at 315px 300px, var(--facade-glow) 0%, rgba(140,144,220,.6) 45%, rgba(140,144,220,0) 80%),
      radial-gradient(ellipse 360px 320px at 315px 260px, rgba(75,84,168,.95) 0%, rgba(59,63,143,.8) 55%, rgba(59,63,143,0) 100%),
      linear-gradient(180deg, rgba(59,63,143,0) 0%, rgba(59,63,143,.55) 35%, rgba(10,15,42,.9) 85%, var(--street-dark) 100%);
    -webkit-mask-image: linear-gradient(180deg, transparent 0%, #000 18%, #000 100%);
            mask-image: linear-gradient(180deg, transparent 0%, #000 18%, #000 100%);
  }

  /* Back cover */
  .back { position: absolute; left: 50px; top: 40px; width: 490px; font-size: 11.3px; line-height: 1.45; }
  .back .hook { text-align: center; font-size: 16px; line-height: 1.3; margin-bottom: 12px; }
  .back p { margin-bottom: 12px; }
  .back ul { list-style: none; margin: 1px 0 12px; }
  .back li { padding-left: 13px; position: relative; }
  .back li::before {
    content: ""; position: absolute; left: 0; top: 4px; width: 7px; height: 9px; border: 1px solid var(--text-white);
  }
  .back .cta { text-align: center; margin-top: 2px; }
  .back .cta strong { display: block; }
  .rule { position: absolute; left: 50px; top: 608px; width: 437px; height: 1px; background: var(--rule); }
  .author-photo {
    position: absolute; left: 50px; top: 628px; width: 146px; height: 110px;
    background: linear-gradient(180deg, #cfcac4 0%, var(--portrait) 55%, #2a2a2e 100%);
    border: 1px solid #ddd;
  }
  .about { position: absolute; left: 209px; top: 626px; width: 335px; font-size: 10.4px; line-height: 1.5; }
  .links { position: absolute; left: 50px; top: 758px; font-size: 10.6px; line-height: 1.5; }

  /* Spine */
  .spine-title, .spine-author {
    position: absolute; writing-mode: vertical-rl; white-space: nowrap;
    font-family: "Oswald", "Arial Narrow", sans-serif; font-weight: 700; letter-spacing: 1px;
  }
  .spine-title { left: 565px; top: 42px; font-size: 34px; color: var(--spine-fill); }
  .spine-author { left: 566px; top: 548px; font-size: 31px; color: var(--text-white); }

  /* Front cover */
  .title {
    position: absolute; left: 640px; top: 18px; width: 540px; text-align: center;
    font-family: "Anton", Impact, sans-serif; color: var(--title-fill);
    -webkit-text-stroke: 2px var(--title-edge);
    text-shadow: 3px 4px 0 rgba(20,30,70,.55);
    line-height: 1; letter-spacing: 3px;
  }
  .title span { display: block; font-size: 104px; margin-bottom: 2px; }
  .subtitle {
    position: absolute; left: 620px; top: 362px; width: 580px; text-align: center;
    font-family: "Oswald", "Arial Narrow", sans-serif; font-weight: 700; font-size: 30px;
    color: var(--text-white); letter-spacing: .5px;
    text-shadow: 2px 2px 0 rgba(10,20,60,.7);
  }
  .subtitle em { font-family: "Arimo", Arial, sans-serif; font-size: 14px; font-weight: 700; }
  .author {
    position: absolute; left: 620px; top: 822px; width: 580px; text-align: center;
    font-family: "Oswald", "Arial Narrow", sans-serif; font-weight: 700; font-size: 34px; letter-spacing: 1.5px;
    color: var(--text-white);
  }
</style>
</head>
<body>
<div class="cover">
  <div class="sky" role="img" aria-label="Dramatic blue sky with sunlit clouds spanning the whole cover"></div>
  <div class="ground"></div>
  <div class="street-scene" role="img" aria-label="Night street scene with a grand lit sports store building between small closing-down shops and silhouetted shoppers"></div>

  <section class="back">
    <p class="hook">Wanted to live the dream of owning a sports store but you’re NOW LIVING A REAL LIFE NIGHTMARE?</p>
    <p class="hook">Do you know sports better than most people, but can’t seem to transition that knowledge to help your sports store grow?</p>
    <p>You most likely have frustrations around a lack of LOYAL customers, you find it really hard to attract and keep quality staff, and, you’re struggling with online pricing?</p>
    <p>A QUIET HARVEST is the book for all you ex-sporting greats and experts who love working with sports &amp; leisure people, but haven’t unlocked how to use it to pay the bills and run a PROFITABLE SPORTS STORE.</p>
    <p>Written specifically for people who have limited retail knowledge but are experts or professionals inside a sporting field, A QUIET HARVEST dulls down the noise and bright shiny lights, and places a set of working priorities in front of you to follow and profit from.</p>
    <div>Inside you’ll learn:</div>
    <ul>
      <li>How to ensure you’re solving your sporting clients problems effectively</li>
      <li>Which retail method is right for your store</li>
      <li>How to manage your inventory effectively</li>
      <li>The best way to market a sports store</li>
      <li>How to recruit and build an INVINCIBLE team, and</li>
      <li>How to deliver remarkable experiences for you clients</li>
    </ul>
    <p class="quote">“Many ex pat sporting greats slap a chunk of money down, open a sports store in a small town and expect the tills to ring… Doesn’t work that way anymore. Customers need more than just a good price. A QUIET HARVEST absolutely helps retail owners and franchisees focus on the important retail aspects and clearly shows how to manage a retail business to greater results, it’s a retail life saver” - Miles Bennet - Director of Crewline Partners</p>
    <p class="cta">If you want more customers, dollars, profits and ultimately time through your sports store then read and uncover the 7 step PREMIER retail method that unlocks <strong>MORE CUSTOMERS, MORE PROFITS, and MORE TIME.</strong></p>
  </section>

  <div class="rule"></div>
  <div class="author-photo" role="img" aria-label="Portrait photo of the author"></div>
  <div class="about">
    About the Author<br>
    Declan Harrow is a retail thought leader and sports retailing specialist. His business The Fennick Crew has advised and consulted to some of Australia’s leading sporting goods retailers including Stride, Peakline Sports, and Silver Spoke Cycles.<br>
    Declan specialises in working with retail teams on sales and selling strategies, retail team recruitment and training, instore layout and visual executions, database &amp; loyalty marketing structures.
  </div>
  <div class="links">
    Visit www.thefennickcrew.com.au for more…<br>
    www.aquietharvest.com.au
  </div>

  <div class="spine-title">A QUIET HARVEST</div>
  <div class="spine-author">DECLAN HARROW</div>

  <h1 class="title"><span>A</span><span>QUIET</span><span>HARVEST</span></h1>
  <div class="subtitle">PROFIT MORE <em>from your</em> SPORTS STORE</div>
  <div class="author">DECLAN HARROW</div>
</div>
</body>
</html>
```